Website Redesign for Pet Services Facility

We are looking to redesign our current website. The website must be designed in Wix so we can go in and easily edit throughout the life of the website. Design must be professional, simplistic and informative.

Our current website can be found at: www.pawlanelodge.com

I would like the new site to be on one scrolling page. Sections to include:
Home page
Service teaser: Overnight Care, Grooming, Dog Daycare, Retail
An about us area with text on the left and a video on the right
Testimonial section
Overnight Section
Grooming Section
Dog Daycare Section
Retail
Meet the Team
Contact us: address, phone number, hours, etc.
Newsletter sign up and location map

A second page will be used for reservations and should include fields for.
Name, address, phone number, service: Overnight care, grooming, daycare, Arrival date, departure date, pet name, breed, special requests

Our phone number should be easily found through the pages. 'Request a Reservation' buttons should be found throughout page.

Text from our current site can be uesd as a filler for now as I will go in and finalize text when site is complete. Any photos can be used for now as I will go in and choose final photos as a later date.

I started playing with wix and started with a concept that I can share if you are interested, just let me know.

Industry/Entity Type

Pet

Number of Pages Required

2 page

Font styles to use
Sans Serif

Requirements
Must have
• 'Request a Reservation' Buttons
• Phone number easily visible
• location map
• Hours area
• Newsletter sign up

```html
<!DOCTYPE html>
<html lang="en">
<head>
<meta charset="utf-8">
<title>Paw Lane Lodge</title>
<link href="https://fonts.googleapis.com/css2?family=Lato:wght@300;400;700&display=swap" rel="stylesheet">
<style>
:root{
  --olive:#4a3f22;
  --green:#9dc230;
  --brown:#4a3f2a;
  --grey:#7a7a7a;
  --pale:#f3f6f6;
  --white:#ffffff;
  --teal:#8cc3cf;
}
*{box-sizing:border-box;margin:0;padding:0}
html,body{width:929px;height:1200px;overflow:hidden}
body{font-family:'Lato',sans-serif;background:var(--white);color:var(--brown);position:relative}
a{text-decoration:none;color:inherit}

.topbar{position:absolute;top:0;left:0;width:929px;height:32px;background:var(--olive);color:var(--white);font-size:8px}
.topbar .welcome{position:absolute;left:87px;top:11px;font-weight:700}
.topbar .right{position:absolute;right:86px;top:9px;display:flex;align-items:center;gap:18px;font-size:9px}
.topbar .right span{display:flex;align-items:center;gap:5px}
.social{display:flex;gap:10px}
.social i{display:block;width:8px;height:8px;border-radius:2px;background:var(--green)}

.header{position:absolute;top:32px;left:0;width:929px;height:88px}
.brand{position:absolute;left:86px;top:30px;display:flex;align-items:center;gap:7px;font-size:15px;font-weight:700;color:var(--olive);letter-spacing:.3px}
.brand .mark{width:26px;height:26px;background:var(--teal)}
.nav{position:absolute;left:256px;top:38px;display:flex;gap:26px;font-size:9px;color:#3a3a3a}
.nav a{padding:0 2px 7px;border-bottom:2px solid transparent;white-space:nowrap}
.nav a.active{border-color:var(--green)}
.call{position:absolute;left:723px;top:29px;width:140px;height:32px;background:var(--green);color:var(--white);border-radius:16px;display:flex;align-items:center;justify-content:center;font-size:8.5px;white-space:nowrap}
.call b{font-weight:400;font-size:12.5px;margin-left:3px}

.hero{position:absolute;top:120px;left:0;width:929px;height:315px;color:var(--white);text-align:center;
  background:
    radial-gradient(ellipse 110px 70px at 680px 225px,rgba(35,25,20,.85),rgba(35,25,20,0)),
    radial-gradient(ellipse 300px 220px at 430px 120px,rgba(190,130,70,.9),rgba(190,130,70,0)),
    linear-gradient(90deg,#9a6736 0%,#b47a43 35%,#a86f3c 60%,#7f6a3a 78%,#5f8f36 90%,#4f8a30 100%)}
.hero h1{font-weight:400;font-size:35px;margin-top:64px;text-shadow:0 1px 3px rgba(0,0,0,.25)}
.hero p{font-size:10.5px;line-height:16px;width:475px;margin:8px auto 0;text-shadow:0 1px 2px rgba(0,0,0,.3)}
.hero .btn{display:inline-block;margin-top:33px;background:var(--green);border-radius:15px;height:30px;line-height:30px;padding:0 20px;font-size:9px;font-weight:700}
.dots{position:absolute;top:292px;left:442px;display:flex;gap:5px}
.dots i{width:6px;height:6px;border-radius:50%;background:var(--white)}
.dots i:first-child{background:none;border:1px solid var(--white)}

.services{position:absolute;top:435px;left:0;width:929px;height:447px;background:var(--pale);text-align:center}
.services h2{font-weight:300;font-size:31px;margin-top:30px;color:var(--brown)}
.rule{width:21px;height:2px;background:var(--green);margin:14px auto 0}
.services .lead{font-size:10.5px;line-height:20px;color:var(--grey);width:380px;margin:11px auto 0}
.card{position:absolute;top:175px;width:172px;height:225px;background:var(--white);padding-top:9px}
.card.active{border-bottom:3px solid var(--green)}
.card .photo{width:75px;height:75px;border-radius:50%;margin:0 auto}
.card h3{font-size:12.5px;font-weight:700;margin-top:13px;color:var(--brown)}
.card p{font-size:10.5px;line-height:16px;color:var(--grey);width:128px;margin:10px auto 0}
.more{display:inline-block;margin-top:12px;font-size:10.5px;color:var(--green)}

.about{position:absolute;top:882px;left:0;width:465px;height:282px;color:var(--white);text-align:center;
  background:radial-gradient(ellipse 160px 120px at 120px 130px,rgba(140,160,60,.5),rgba(140,160,60,0)),radial-gradient(ellipse 150px 110px at 330px 90px,rgba(190,210,110,.45),rgba(190,210,110,0)),#a1c435}
.about h2{font-weight:300;font-size:31px;margin-top:45px}
.about .rule{background:var(--white);margin-top:12px}
.about p{font-size:10.5px;line-height:23.3px;width:310px;margin:14px auto 0}
.about .more{color:var(--white);margin-top:10px}
.video{position:absolute;top:882px;left:465px;width:464px;height:282px;
  background:
    radial-gradient(ellipse 170px 190px at 240px 150px,rgba(128,116,108,.95),rgba(128,116,108,0)),
    radial-gradient(ellipse 120px 40px at 200px 250px,rgba(190,80,90,.6),rgba(190,80,90,0)),
    linear-gradient(160deg,#a8ae86 0%,#86a452 40%,#6c9038 100%)}
.play{position:absolute;left:194px;top:100px;width:76px;height:76px}
</style>
</head>
<body>
<div class="topbar">
  <span class="welcome">Welcome to The Paw Lane Lodge website!</span>
  <div class="right">
    <span><svg width="9" height="8" viewBox="0 0 9 8"><path d="M0 1h2l1 4h5l1-3H3" fill="none" stroke="#9dc230"/><circle cx="3.5" cy="7" r="1" fill="#9dc230"/><circle cx="7" cy="7" r="1" fill="#9dc230"/></svg>Your Cart: 0 item - $0.00</span>
    <span><svg width="8" height="8" viewBox="0 0 8 8"><circle cx="4" cy="2.5" r="2" fill="none" stroke="#9dc230"/><path d="M0.5 8c0-3 7-3 7 0" fill="none" stroke="#9dc230"/></svg>Log in</span>
    <div class="social" aria-label="Social links"><i></i><i></i><i></i><i></i></div>
  </div>
</div>

<header class="header">
  <div class="brand"><span class="mark"></span>Paw Lane Lodge</div>
  <nav class="nav">
    <a class="active">About Us</a><a>Daycare</a><a>Overnight Care</a><a>Grooming</a><a>Shop</a><a>Resources</a><a>Contact Us</a>
  </nav>
  <a class="call">Call Us : <b>920.555.0148</b></a>
</header>

<section class="hero" role="img" aria-label="Close-up photo of a golden puppy resting on grass">
  <h1>Pet Services &amp; Dog Walking</h1>
  <p>Lorem Ipsum is simply dummy text of the printing and typesetting industry. Lorem Ipsum has been the industry's standard dummy text ever since . the 1500s, when an unknown printer took a galley of type and scrambled it to make a type specimen book.</p>
  <a class="btn">MORE INFORATON &#8250;</a>
  <div class="dots"><i></i><i></i><i></i><i></i></div>
</section>

<section class="services">
  <h2>We Provide Best Services</h2>
  <div class="rule"></div>
  <p class="lead">There are many variations of passages of Lorem Ipsum available, but the majority have suffered alteration in some form, by injected humour,</p>

  <div class="card active" style="left:82px">
    <div class="photo" role="img" aria-label="Photo of a dog and a cat together" style="background:radial-gradient(circle at 55% 55%,#6e4a2e 0%,#9a7a5c 40%,#d8d2ca 80%)"></div>
    <h3>Overnight Care</h3>
    <p>Leaving your pet overnight should not be a stressful time for either of you.</p>
    <a class="more">Learn more &#8250;</a>
  </div>
  <div class="card" style="left:278px">
    <div class="photo" role="img" aria-label="Photo of a small dog being groomed" style="background:radial-gradient(circle at 50% 45%,#f0c89a 0%,#d48a4a 45%,#8e3e22 90%)"></div>
    <h3>Grooming</h3>
    <p>Grooming at Paw Lane Lodge is truly all about the client.</p>
    <a class="more">Learn more &#8250;</a>
  </div>
  <div class="card" style="left:478px">
    <div class="photo" role="img" aria-label="Photo of dogs playing at daycare" style="background:radial-gradient(circle at 45% 70%,#c8c8c0 0%,#5e5e5a 40%,#262626 85%)"></div>
    <h3>Dog Daycare</h3>
    <p>Socialization is one of the most important aspects of canine development.</p>
    <a class="more">Learn more &#8250;</a>
  </div>
  <div class="card" style="left:674px">
    <div class="photo" role="img" aria-label="Photo of a shopper holding a puppy in the store" style="background:radial-gradient(circle at 55% 55%,#d9b8a8 0%,#4a3a40 35%,#a8303a 70%,#3a5a9a 95%)"></div>
    <h3>Retail</h3>
    <p>As a part of our dedication to the health and happiness of your pets</p>
    <a class="more">Learn more &#8250;</a>
  </div>
</section>

<section class="about">
  <h2>About Us</h2>
  <div class="rule"></div>
  <p>In early 2007 we were looking for a place in the Maple Valley for our dogs to stay overnight. Some places would not give a tour. Others were smelly. There were harsh surfaces such as gravel in some of the play areas. Some facilities did not offer daycare options or used cages and crates.</p>
  <a class="more">Learn more &#8250;</a>
</section>
<div class="video" role="img" aria-label="Video still of a grey puppy carrying a rope toy on grass">
  <svg class="play" viewBox="0 0 76 76"><circle cx="38" cy="38" r="38" fill="rgba(255,255,255,.25)"/><path d="M32 26l16 12-16 12z" fill="rgba(255,255,255,.7)"/></svg>
</div>
</body>
</html>
```